Dance Card to Provide Contact Info

I'm looking for a double sided business card to provide contact information to perspective dance partners.
One side of the card would have the words: "Yes I would love to Dance" written in an interesting and eye catching way. Below that would be the three categories I'm interested in
>Social >Exhibition >Competition
The other side of the card would include a picture of me with my Name, Phone Number, and Email Address (Dale Pruitt, 210-574-1328, dale@twirlnstep.dance)
My target market is middle aged women interested in Country and Western dancing and West Coast Swing dancing. I am NOT particularly interested in Ballroom style.
Here are a few links to the type of dancing I want to do:
http://www.plvkrn.org/
http://www.prairiefolkstepsociety.com/
http://mesquitevalleytwostep.com/
Dale Pruitt
210-574-1328
dale@twirlnstep.dance

```html
<!DOCTYPE html>
<html lang="en">
<head>
<meta charset="utf-8">
<title>Dale Pruitt – Dance Card</title>
<link rel="stylesheet" href="https://fonts.googleapis.com/css2?family=Alex+Brush&family=Playball&family=Raleway:wght@400;500;600;800&display=swap">
<style>
  :root {
    --backdrop: #d9d9d9;
    --card: #ffffff;
    --ink: #1c1c1c;
    --mark-grey: #a3a3a3;
    --rule: #cfcfcf;
    --photo-light: #d9a98a;
    --photo-dark: #1b1b1b;
  }
  * { box-sizing: border-box; margin: 0; padding: 0; }
  html, body {
    width: 1105px; height: 1200px; overflow: hidden;
    background: var(--backdrop);
  }
  .canvas { position: relative; width: 1105px; height: 1200px; }
  .card {
    position: absolute; left: 192px; width: 720px; height: 412px;
    background: var(--card); overflow: hidden;
  }
  .card--front { top: 145px; }
  .card--back { top: 602px; }

  /* Contact side */
  .brand {
    position: absolute; left: 40px; top: 40px;
    display: flex; align-items: center; gap: 12px;
    font-family: "Raleway", sans-serif; font-weight: 600;
    font-size: 20px; letter-spacing: 3px; color: var(--mark-grey);
  }
  .brand__dot { width: 20px; height: 20px; border-radius: 50%; background: var(--mark-grey); }
  .contact {
    position: absolute; right: 286px; top: 222px;
    text-align: right; color: var(--ink);
  }
  .contact__name {
    font-family: "Alex Brush", cursive; font-weight: 400;
    font-size: 58px; line-height: 1; margin-bottom: 22px; white-space: nowrap;
  }
  .contact__line {
    font-family: "Raleway", sans-serif; font-weight: 500; font-size: 20px;
    line-height: 32px; white-space: nowrap;
  }
  .contact__email { letter-spacing: 0.5px; }
  .portrait {
    position: absolute; right: 0; bottom: 0; width: 264px; height: 412px;
    background: linear-gradient(180deg, var(--photo-light) 0%, #c88a6a 45%, var(--photo-dark) 62%, var(--photo-dark) 100%);
  }

  /* Slogan side */
  .slogan {
    position: absolute; inset: 0;
    display: flex; flex-direction: column; align-items: center; justify-content: center;
    color: var(--ink); text-align: center;
  }
  .slogan__yes {
    font-family: "Playball", cursive; font-size: 64px; line-height: 1;
  }
  .slogan__love {
    margin-top: 6px;
    font-family: "Raleway", sans-serif; font-weight: 800; font-size: 28px;
    letter-spacing: 2px;
  }
  .slogan__dance {
    font-family: "Playball", cursive; font-size: 120px; line-height: 1.1;
  }
  .slogan__rule { width: 360px; height: 1px; background: var(--rule); margin: 8px 0 14px; }
  .slogan__styles {
    font-family: "Raleway", sans-serif; font-weight: 500; font-size: 20px;
    letter-spacing: 1.5px;
  }
</style>
</head>
<body>
<main class="canvas">
  <section class="card card--front" aria-label="Contact side">
    <div class="brand"><span class="brand__dot"></span>TWIRL N STEP</div>
    <div class="portrait" role="img" aria-label="Portrait photo of Dale Pruitt in a black shirt"></div>
    <div class="contact">
      <h1 class="contact__name">Dale Pruitt</h1>
      <p class="contact__line contact__phone">210-574-1328</p>
      <p class="contact__line contact__email">DALE@TWIRLNSTEP.DANCE</p>
    </div>
  </section>

  <section class="card card--back" aria-label="Slogan side">
    <div class="slogan">
      <span class="slogan__yes">Yes</span>
      <span class="slogan__love">I WOULD LOVE TO</span>
      <span class="slogan__dance">Dance</span>
      <span class="slogan__rule"></span>
      <span class="slogan__styles">SOCIAL • EXHIBITION • COMPETITION</span>
    </div>
  </section>
</main>
</body>
</html>
```